postcard/flyer for Ridgeway Strength

I need a 4x6 postcard design (front and back) to advertise our business. It is a gym for serious athletes or for people who don't mind a sweat when they workout. Our focus is boxing, functional fitness (like PulseDrill), and personal training. We are opening October 1 and want to pass these out at local business. We want to include the name, address, website, phone, and possibly some photos of our space. We want to cater to men, women, and children. Please refer to our website for content: www.ridgewaystrength.example
Updates

Thank you designers for your submissions. I like that you have all been looking to the website for photos and colors and inspiration. Now I am wondering if you can change it up a little! We want to attract more women and even kids, while still incorporating our logo and some actual pictures of the space. Right now, all the designs seem a little too tough and masculine. I know I am somewhat contradicting myself but I know it is possible. Perhaps suggest power with graphic patterns, or accent colors! Or overlays in a lighter color or making the photos monochomatic in a more feminine color. Our other accent colors in the gym space are actually rich yellow, orange juice orange, and bright lime green. Thank you so much!

Project Deadline Extended
Reason: I am extending the deadline! I am interested in seeing more submissions! Thank you!

Industry/Entity Type

Fitness

```html
<!DOCTYPE html>
<html lang="en">
<head>
<meta charset="utf-8">
<title>Ridgeway Strength – Postcard Front and Back</title>
<link href="https://fonts.googleapis.com/css2?family=Audiowide&family=Montserrat:wght@600;700;800&display=swap" rel="stylesheet">
<style>
  :root {
    --stage: #3b3b3d;
    --paper: #ffffff;
    --mist: #e6e7e8;
    --ink: #1a1a1a;
    --steel: #6d6e71;
    --faint: #ececec;
    --yellow: #ffe600;
    --orange: #f7941d;
    --lime: #c4d82e;
    --rule: #9a9a9a;
  }
  * { box-sizing: border-box; margin: 0; padding: 0; }
  html, body { width: 968px; height: 1200px; overflow: hidden; background: var(--stage); }
  body { position: relative; font-family: "Montserrat", Arial, sans-serif; color: var(--ink); }

  .card { position: absolute; left: 101px; width: 764px; height: 510px; overflow: hidden; }
  .card--front { top: 66px; background: var(--mist); }
  .card--back { top: 615px; background: var(--paper); }
  .bands { position: absolute; inset: 0; width: 100%; height: 100%; }

  .wordmark { position: absolute; font-weight: 800; color: var(--steel); text-transform: uppercase; line-height: 1.05; letter-spacing: 1px; }
  .card--front .wordmark { left: 42px; top: 78px; font-size: 25px; }
  .card--back .wordmark { left: 262px; top: 292px; font-size: 23px; }
  .card--back .wordmark--faint { color: var(--faint); left: 493px; top: 330px; font-size: 32px; }

  .contact-top { position: absolute; right: 33px; top: 30px; text-align: right; font-size: 14px; font-weight: 600; line-height: 1.5; }
  .contact-top .web { font-weight: 700; font-size: 16px; }

  .tagline, .services { position: absolute; font-family: "Audiowide", sans-serif; line-height: 1; transform-origin: left bottom; transform: rotate(-8.8deg); white-space: nowrap; color: var(--ink); }
  .tagline { left: 333px; top: 158px; font-size: 21px; }
  .services { left: 168px; top: 476px; font-size: 19px; }

  .call { position: absolute; right: 33px; top: 442px; text-align: right; font-weight: 700; font-size: 17px; line-height: 1.35; }

  .photos { position: absolute; display: flex; }
  .card--front .photos { left: 0; top: 0; width: 764px; height: 510px; clip-path: polygon(0 213px, 764px 161px, 764px 374px, 0 422px); }
  .card--back .photos { left: 0; top: 0; width: 431px; height: 195px; clip-path: polygon(0 0, 431px 0, 431px 129px, 0 193px); }
  .photo { height: 100%; }
  .photo--gym-floor { width: 236px; background: linear-gradient(160deg, #3d5b7a 0%, #8d8e8a 45%, #c9aa78 70%, #2f6b3c 100%); }
  .photo--rig { width: 284px; background: linear-gradient(180deg, #e3e1dc 0%, #a8a6a1 50%, #5d5a55 100%); }
  .photo--balls { width: 244px; background: linear-gradient(150deg, #5a6b5b 0%, #3c8f7c 45%, #d23a8d 75%, #5aa43a 100%); }
  .card--back .photo--gym-floor { width: 219px; }
  .photo--coach { width: 212px; background: linear-gradient(180deg, #d9d7d2 0%, #6f7590 55%, #3f4148 100%); }

  .back-info { position: absolute; left: 27px; top: 252px; font-size: 14px; font-weight: 600; line-height: 1.45; }
  .back-info p + p { margin-top: 18px; }
  .back-info .strong { font-weight: 700; }

  .stamp { position: absolute; left: 644px; top: 41px; width: 88px; height: 106px; border: 1.5px solid var(--rule); }
  .address-line { position: absolute; left: 470px; width: 260px; border-top: 1.5px solid var(--rule); }
  .address-line--1 { top: 285px; }
  .address-line--2 { top: 342px; }
  .address-line--3 { top: 399px; }
  .address-line--4 { top: 457px; }
</style>
</head>
<body>

<section class="card card--front" aria-label="Postcard front">
  <svg class="bands" viewBox="0 0 764 510" aria-hidden="true">
    <polygon points="0,197 764,73 764,161 0,213" fill="var(--yellow)"/>
    <polygon points="0,422 608,384 0,457" fill="var(--orange)"/>
    <polygon points="0,457 608,384 764,374 764,510 0,510" fill="var(--lime)"/>
  </svg>

  <div class="wordmark">Ridgeway<br>Strength</div>

  <div class="contact-top">
    <p>4820 Harbor Row Lakeview, CA 90210</p>
    <p class="web">ridgewaystrength.example</p>
  </div>

  <p class="tagline">For men, women, and children.</p>

  <div class="photos">
    <div class="photo photo--gym-floor" role="img" aria-label="Photo of the gym floor with wooden plyo boxes and lockers"></div>
    <div class="photo photo--rig" role="img" aria-label="Photo of the training rig with rings, bumper plates and barbells"></div>
    <div class="photo photo--balls" role="img" aria-label="Photo of medicine balls and balance trainers on turf"></div>
  </div>

  <p class="services">boxing || functional fitness || personal training</p>

  <div class="call">
    <p>Call Us:</p>
    <p>555-014-GRIP (4747)</p>
  </div>
</section>

<section class="card card--back" aria-label="Postcard back">
  <svg class="bands" viewBox="0 0 764 510" aria-hidden="true">
    <polygon points="0,191 431,129 431,174 0,215" fill="var(--yellow)"/>
    <polygon points="0,449 431,413 431,440 0,461" fill="var(--orange)"/>
    <polygon points="0,461 431,440 431,510 0,510" fill="var(--lime)"/>
  </svg>

  <div class="photos">
    <div class="photo photo--gym-floor" role="img" aria-label="Photo of the gym floor with wooden plyo boxes"></div>
    <div class="photo photo--coach" role="img" aria-label="Photo of a trainer skipping rope in the gym"></div>
  </div>

  <div class="back-info">
    <p>4820 Harbor Row Lakeview,<br>CA 90210</p>
    <p class="strong">ridgewaystrength.example</p>
    <p class="strong">Call Us:<br>555-014-GRIP (4747)</p>
  </div>

  <div class="wordmark">Ridgeway<br>Strength</div>
  <div class="wordmark wordmark--faint" aria-hidden="true">Ridgeway<br>Strength</div>

  <div class="stamp" aria-label="Stamp area"></div>
  <div class="address-line address-line--1"></div>
  <div class="address-line address-line--2"></div>
  <div class="address-line address-line--3"></div>
  <div class="address-line address-line--4"></div>
</section>

</body>
</html>
```